PC & LAPTOP REPAIR site design custom wordpress theme

Need a wordpress theme that is customized and can be upgraded without losing content, look.

Byte quickMEND we provide a fast affordable pc/ laptop service that comes to you. We aim to provide same day service. I can add most of the text content i need a working theme with 5 pages, my logo. I have provided the layout i am after. This is the orange image.
I have provided my logo, the colour and some words.
I need your design skills at the same time i'm very much after the layout of the orange images FILE 1/4/5 . But with my logo and my colours the blue and black.

5 buttons beneath header. The old , ABOUT US, CONTACT US, HELP, PAYMENT, EMPLOYMENT ? That lead to pages i can edit my self. And 2 or 3 flashing cheesy images where the old man is in layout picture. Preferable a family or attractive female pc technician? as if they exist. joke im sure they do.

Also a box on index page query or quote. That people can simple fill and email. a simple php script maybe? however im happy.

I want to be able to edit page text myself, upgrade wordpress not lose layout, (upgrade and editable page friendly) WITH my blue my logo, my blue color theme

1ST 4TH 5TH fileS ARE the layout im after .

2nd. My logo and theme and color to be used in the layout of file 1.

3rd. Just some text and swirls that might be useful.

Reason: Have to visit family in Western Australia. Will be back in Melbourne 4th December.

Requirements
Must have
• My logo Byte quickMEND
My colour scheme that exact blue, with grey, black or white.
Same layout as image provided.
Can be upgraded and editable text.
Nice to have
• mobile device happy?
Should not have
• contact box quote or query?

```html
<!DOCTYPE html>
<html lang="en">
<head>
<meta charset="utf-8">
<title>Byte quickMEND — PC &amp; Laptop Repair</title>
<link rel="stylesheet" href="https://fonts.googleapis.com/css2?family=Roboto+Condensed:wght@300;400;700&family=PT+Sans:wght@400;700&display=swap">
<style>
:root{
  --blue:#3a86c8;
  --blue-deep:#3a6fc0;
  --nav:#3a3a3a;
  --nav-active:#6f6f6f;
  --ink:#2a2a2a;
  --muted:#555;
  --panel:#f6f6f6;
  --line:#9a9a9a;
  --foot:#2f2f2f;
  --foot-base:#262626;
  --foot-text:#d8d8d8;
  --foot-head:#8d8d8d;
}
*{margin:0;padding:0;box-sizing:border-box}
html,body{width:963px;height:1200px;overflow:hidden;background:#fff}
.page{position:absolute;left:0;top:0;width:1200px;height:1495px;transform:scale(.8025);transform-origin:0 0;font-family:"PT Sans",sans-serif;color:var(--ink)}
.abs{position:absolute}

/* header */
.masthead{left:0;top:0;width:1200px;height:131px;background:linear-gradient(#e4e4e4,#fff 30%)}
.brand{left:92px;top:50px;font-family:"PT Sans",sans-serif;font-weight:400;font-size:42px;color:var(--ink);white-space:nowrap}
.callout{left:696px;top:38px;font-family:"Roboto Condensed",sans-serif;font-weight:300;font-size:36px;color:#333;line-height:1}
.phone{left:696px;top:78px;font-family:"Roboto Condensed",sans-serif;font-weight:300;font-size:18px;color:#333;display:flex;align-items:center;gap:7px}
.social{left:922px;top:54px;display:flex;gap:10px}
.social span{width:40px;height:40px;border-radius:50%;background:#2b5ca8}

/* nav */
.nav{left:0;top:131px;width:1200px;height:56px;background:var(--nav);border-bottom:5px solid var(--blue-deep)}
.nav a{position:absolute;top:0;height:51px;line-height:52px;text-align:center;color:#fff;font-weight:700;font-size:14px;text-decoration:none;border-right:1px solid #555}
.nav a.active{background:var(--nav-active);border-right:none}
.search{left:876px;top:9px;width:236px;height:30px;border-radius:15px;background:#fff;font-size:13px;color:#444;padding:6px 15px}
.search svg{position:absolute;right:12px;top:8px}

/* hero */
.hero{left:88px;top:187px;width:1024px;height:429px;background:var(--panel);border-bottom:1px solid var(--line)}
.hero-photo{left:12px;top:8px;width:480px;height:421px;background:linear-gradient(135deg,#e9ddd6 0%,#d98ab4 45%,#c5c5c5 80%,#f6f6f6 100%);border-radius:180px 120px 0 0}
.trouble{left:375px;top:76px;width:619px;height:54px;background:var(--blue-deep);color:#fff;font-family:Arial,sans-serif;font-size:68px;line-height:56px;text-align:center;letter-spacing:1px;white-space:nowrap}
.connect{right:30px;top:132px;font-family:"Roboto Condensed",sans-serif;font-weight:300;font-size:60px;color:#333;letter-spacing:-1.5px;white-space:nowrap}
.hero-copy{right:30px;top:202px;width:490px;text-align:right;font-size:13.5px;line-height:24px;color:#333}
.read-more{left:887px;top:288px;width:106px;height:39px;background:var(--blue);color:#fff;font-size:13px;line-height:39px;text-align:center}
.slide-arrows{left:898px;top:353px;display:flex;gap:2px}
.slide-arrows span{width:46px;height:46px;background:#8a8a8a;display:flex;align-items:center;justify-content:center}
.slide-ctrl{left:460px;top:394px}

/* tagline */
.tagline{left:88px;top:636px;width:1024px;text-align:center;font-family:"Roboto Condensed",sans-serif;font-weight:300;font-size:36px;color:#333;letter-spacing:-.8px;white-space:nowrap}
.tagline-sub{left:88px;top:676px;width:1024px;text-align:center;font-family:"Roboto Condensed",sans-serif;font-weight:300;font-size:17px;color:#333;white-space:nowrap}
.rule{left:88px;top:716px;width:1024px;height:1px;background:var(--line)}

/* feature boxes */
.card{top:751px;width:230px;height:327px;background:linear-gradient(#fff 70%,#ececec);border:1px solid #ddd;border-top:4px solid #888}
.card h2{height:40px;background:var(--blue);color:#fff;font-family:"Roboto Condensed",sans-serif;font-weight:300;font-size:25px;line-height:42px;padding-left:20px;white-space:nowrap}
.card .btn{position:absolute;right:16px;bottom:13px;width:72px;height:27px;border-radius:10px;background:#1e1e1e;color:#fff;font-size:14px;line-height:27px;text-align:center}
.field{margin:12px 12px 0;height:31px;border:1px solid #ccc;border-radius:4px;font-size:13px;padding:7px 11px;color:#222}
.field.tall{height:58px}
.ticks{list-style:none;padding:20px 6px 0 24px}
.ticks li{position:relative;padding-left:28px;font-size:13.5px;line-height:14px;color:#444;margin-bottom:14px}
.ticks li svg{position:absolute;left:0;top:0}
.help-copy{padding:18px 0 0 25px;font-family:"Roboto Condensed",sans-serif;font-weight:300;font-size:19px;color:#333;line-height:36px;white-space:nowrap}
.help-copy em{font-style:normal;color:var(--blue);font-size:24px;letter-spacing:-.3px}

/* footer */
.footer{left:0;top:1110px;width:1200px;height:318px;background:radial-gradient(ellipse at 45% 0%,#3a3a3a,var(--foot) 60%)}
.foot-head{font-weight:700;font-size:18px;color:var(--foot-head)}
.divider{top:28px;width:1px;height:252px;background:#555}
.links{list-style:none;margin-top:22px}
.links li{font-size:13.5px;color:var(--foot-text);margin-bottom:7px;display:flex;align-items:center;gap:8px}
.post{display:flex;gap:18px}
.post-thumb{width:58px;height:56px;border-radius:6px;background:linear-gradient(135deg,#f1e6d8,#c9a98c)}
.post p{font-size:11px;line-height:18px;color:var(--foot-text);width:132px;text-align:justify}
.testimonial{font-size:11px;line-height:18px;color:var(--foot-text);width:266px;text-align:justify}
.sign{font-weight:700;font-size:17px;color:#fff;text-align:right;width:266px}
.input{width:258px;height:35px;border-radius:6px;background:#111;border:1px solid #444;font-size:14px;color:#888;padding:8px 11px;margin-bottom:18px}
.input.msg{height:65px}
.submit{left:1041px;top:261px;width:71px;height:27px;border-radius:6px;background:var(--blue);color:#fff;font-size:14px;line-height:27px;text-align:center}
.base{left:0;top:1428px;width:1200px;height:67px;background:var(--foot-base);text-align:center;font-size:11.5px;color:#ddd;line-height:64px}
</style>
</head>
<body>
<div class="page">

  <header class="abs masthead">
    <div class="abs brand">Byte quickMEND</div>
    <div class="abs callout">24/7 Call Out</div>
    <div class="abs phone">
      <svg width="9" height="12" viewBox="0 0 9 12"><rect x="1" y="1" width="7" height="10" rx="1.5" fill="none" stroke="#2b5ca8" stroke-width="1.5"/></svg>
      0400 555 128
    </div>
    <div class="abs social" aria-label="Social links"><span></span><span></span><span></span><span></span></div>
  </header>

  <nav class="abs nav">
    <a class="active" style="left:88px;width:122px">ABOUT US</a>
    <a style="left:210px;width:187px">CONTACT US</a>
    <a style="left:397px;width:131px">HELP</a>
    <a style="left:528px;width:146px">PAYMENT</a>
    <a style="left:674px;width:182px;border-right:none">EMPLOYMENT</a>
    <div class="abs search">Search
      <svg width="14" height="14" viewBox="0 0 14 14"><circle cx="8" cy="6" r="4" fill="none" stroke="#3a70c0" stroke-width="2"/><line x1="5" y1="9" x2="1.5" y2="12.5" stroke="#3a70c0" stroke-width="2"/></svg>
    </div>
  </nav>

  <section class="abs hero">
    <div class="abs hero-photo" role="img" aria-label="Photo of a smiling young woman in a pink striped top holding an open laptop"></div>
    <div class="abs trouble">HAVING TROUBLE</div>
    <div class="abs connect">Connecting to the internet</div>
    <p class="abs hero-copy">Lorem Ipsum is simply dummy text of the printing and typesetting industry. Lorem Ipsum has been the industry's standard dummy text ever since the 1500s Lorem Ipsum is simply dummy text of the printing and typesetting industry.</p>
    <div class="abs read-more">Read More</div>
    <div class="abs slide-arrows">
      <span><svg width="16" height="28" viewBox="0 0 16 28"><polyline points="14,2 2,14 14,26" fill="none" stroke="#fff" stroke-width="1.5"/></svg></span>
      <span><svg width="16" height="28" viewBox="0 0 16 28"><polyline points="2,2 14,14 2,26" fill="none" stroke="#fff" stroke-width="1.5"/></svg></span>
    </div>
    <svg class="abs slide-ctrl" width="110" height="18" viewBox="0 0 110 18">
      <polygon points="2,3 12,8 2,13" fill="none" stroke="#777" stroke-width="1.2"/>
      <rect x="20" y="3" width="4" height="10" fill="none" stroke="#777"/><rect x="26" y="3" width="4" height="10" fill="none" stroke="#777"/>
      <circle cx="51" cy="8" r="6" fill="#eee" stroke="#888"/><circle cx="73" cy="8" r="6" fill="#eee" stroke="#888"/><circle cx="95" cy="8" r="6" fill="#eee" stroke="#888"/>
    </svg>
  </section>

  <h1 class="abs tagline">Tempor Incididunt Dolore. Excepteur Sint Occaecat. Cupidatat Non Proident</h1>
  <p class="abs tagline-sub">Lorem ipsum dolor sit amet, consectetur adipisicing elit, sed do eiusmod tempor incididunt ut labore et dolore magna aliqua.</p>
  <div class="abs rule"></div>

  <section class="abs card" style="left:88px">
    <h2>BOOK A JOB</h2>
    <div class="field">First Name</div>
    <div class="field" style="margin-top:9px">Last Name</div>
    <div class="field" style="margin-top:9px">Email</div>
    <div class="field" style="margin-top:9px">Contact Number</div>
    <div class="field tall" style="margin-top:9px">How can we help?</div>
    <div class="btn">More</div>
  </section>

  <section class="abs card" style="left:354px">
    <h2>ABOUT US</h2>
    <ul class="ticks">
      <li><svg width="14" height="12"><polyline points="1,6 5,10 13,1" fill="none" stroke="#3a86c8" stroke-width="2.4"/></svg>We Will come to you,<br>We Provide.</li>
      <li><svg width="14" height="12"><polyline points="1,6 5,10 13,1" fill="none" stroke="#3a86c8" stroke-width="2.4"/></svg>We will tell you where you went wrong.</li>
      <li><svg width="14" height="12"><polyline points="1,6 5,10 13,1" fill="none" stroke="#3a86c8" stroke-width="2.4"/></svg>We Will come to you,<br>We Provide.</li>
      <li><svg width="14" height="12"><polyline points="1,6 5,10 13,1" fill="none" stroke="#3a86c8" stroke-width="2.4"/></svg>We will tell you where you went wrong.</li>
      <li><svg width="14" height="12"><polyline points="1,6 5,10 13,1" fill="none" stroke="#3a86c8" stroke-width="2.4"/></svg>We Will come to you,<br>We Provide.</li>
    </ul>
    <div class="btn" style="right:20px">More</div>
  </section>

  <section class="abs card" style="left:619px">
    <h2>PC HEALTH CHECK</h2>
    <ul class="ticks">
      <li><svg width="14" height="12"><polyline points="1,6 5,10 13,1" fill="none" stroke="#3a86c8" stroke-width="2.4"/></svg>No Call Out Fee</li>
      <li><svg width="14" height="12"><polyline points="1,6 5,10 13,1" fill="none" stroke="#3a86c8" stroke-width="2.4"/></svg>Same Day Onsite Services</li>
      <li><svg width="14" height="12"><polyline points="1,6 5,10 13,1" fill="none" stroke="#3a86c8" stroke-width="2.4"/></svg>Install New Hardware, Video, Sound cards, memory, harddrives, CDRom's Etc.</li>
      <li><svg width="14" height="12"><polyline points="1,6 5,10 13,1" fill="none" stroke="#3a86c8" stroke-width="2.4"/></svg>PC Virus, Trojan Removal and Internet Privacy</li>
      <li><svg width="14" height="12"><polyline points="1,6 5,10 13,1" fill="none" stroke="#3a86c8" stroke-width="2.4"/></svg>PC Problems Solved in Plain English</li>
    </ul>
    <div class="btn" style="right:19px">More</div>
  </section>

  <section class="abs card" style="left:883px">
    <h2>HELP</h2>
    <div class="help-copy">FAST, SAME DAY<br>AND <em>EXPERT ONSITE</em><br>HELP FOR<br>ANYTHING<br><em>COMPUTER RELATED</em></div>
    <div class="btn">More</div>
  </section>

  <footer class="abs footer">
    <div class="abs" style="left:88px;top:26px">
      <div class="foot-head">QUICK LINKS</div>
      <ul class="links">
        <li>&rarr; Home</li><li>&rarr; About Us</li><li>&rarr; Contact Us</li><li>&rarr; Help</li>
        <li>&rarr; Payment</li><li>&rarr; Employment</li><li>&rarr; Book a Job</li><li>&rarr; Customers</li>
      </ul>
    </div>
    <div class="abs divider" style="left:267px"></div>
    <div class="abs" style="left:285px;top:26px">
      <div class="foot-head" style="margin-bottom:22px">RECENT POSTS</div>
      <div class="post"><div class="post-thumb" role="img" aria-label="Post thumbnail photo"></div><p>Lorem Ipsum is simply dummy text of the printing and typesetting industry.</p></div>
      <div class="post" style="margin-top:15px"><div class="post-thumb" role="img" aria-label="Post thumbnail photo"></div><p>Lorem Ipsum is simply dummy text of the printing and typesetting industry.</p></div>
      <div class="post" style="margin-top:15px"><div class="post-thumb" role="img" aria-label="Post thumbnail photo"></div><p>Lorem Ipsum is simply dummy text of the printing and typesetting industry.</p></div>
    </div>
    <div class="abs divider" style="left:528px"></div>
    <div class="abs" style="left:550px;top:26px">
      <div class="foot-head" style="margin-bottom:20px">TESTIMONIALS</div>
      <p class="testimonial">Lorem Ipsum is simply dummy text of the printing and typesetting industry. Lorem Ipsum has been the industry's standard dummy text ever since the 1500s Lorem Ipsum is simply dummy text of the printing and typesetting industry. Lorem Ipsum has been the industry's standard dummy text ever since the 1500s.</p>
      <p class="testimonial" style="margin-top:18px">Lorem Ipsum is simply dummy text of the printing and typesetting industry.</p>
      <p class="sign" style="margin-top:12px">- Lorem Lipsum</p>
    </div>
    <div class="abs divider" style="left:838px"></div>
    <div class="abs" style="left:852px;top:26px">
      <div class="foot-head" style="margin-bottom:16px">CONTACT US</div>
      <div class="input">Name</div>
      <div class="input">Email</div>
      <div class="input msg">Message</div>
    </div>
    <div class="abs submit">Submit</div>
  </footer>

  <div class="abs base">Copyrights &copy; 2012. All Rights Reserved.</div>
</div>
</body>
</html>
```